Business Cards Needed for Innovative Healthcare Marketing Company

We are a marketing company focused on healthcare. Our company is all about rebranding yourself renewing your image and generating results. The phoenix stands for "reborn" or "rising" which we provide new brands for our clients we take their old brands and renew it with creativity and innovation. I am looking for a business card with color dimension. I have attached an example of a card I think has the look and feel of what I am trying to accomplish. I like that the card example has black and grey font colors, I like the font placement and the small logo, I really like the use of the colors on the right those are the colors of my logo. My logo is phoenix so maybe incorporating flames similar to that design. I would like the back a solid color maybe red with an opaque version of the logo and website. As a marketing company I am always open to creative liberty!

Target Market(s)

Doctors and business professionals.

Industry/Entity Type

Marketing

Contact Information for Business Card

Vornaly Health Care Marketing
Marnie Okonski- CEO
#(502)638-2947
email-marnie@vornaly.com
website- vornaly.com

Font styles to use
Sans Serif

Colors
ec1f27
f37122
ffc214
fbed22
fbf289
f04a50

Requirements
Must have
• The logo and required information
Nice to have
• icons by the information
Should not have
• child like font

```html
<!DOCTYPE html>
<html lang="en">
<head>
<meta charset="utf-8">
<title>Vornaly Health Care Marketing – Business Card</title>
<link rel="stylesheet" href="https://fonts.googleapis.com/css2?family=Open+Sans:wght@300;400;700&display=swap">
<style>
  :root {
    --backdrop: #ece9e6;
    --card-white: #ffffff;
    --brand-red: #a8231f;
    --text-dark: #2b2b2b;
    --rule-grey: #c9c9c9;
    --ember-orange: #e8822c;
    --ember-mid: #c9472a;
    --deep-red: #a11f22;
    --ghost-white: rgba(255,255,255,0.9);
  }
  * { box-sizing: border-box; margin: 0; padding: 0; }
  html, body {
    width: 1200px; height: 1000px; overflow: hidden;
    background: var(--backdrop);
    font-family: "Open Sans", Arial, sans-serif;
  }
  .canvas { position: relative; width: 1200px; height: 1000px; }

  .card {
    position: absolute; left: 265px; width: 665px; height: 397px;
    border-radius: 22px; overflow: hidden;
    box-shadow: 0 6px 18px rgba(0,0,0,0.18);
  }
  .card-front { top: 73px; background: var(--card-white); }
  .card-back {
    top: 533px;
    background: radial-gradient(circle at 165px 215px, var(--ember-orange) 0%, var(--ember-mid) 55%, var(--deep-red) 85%);
  }

  .emblem-area {
    position: absolute; border-radius: 50%;
  }
  .card-front .emblem-area {
    left: 10px; top: 60px; width: 330px; height: 330px;
    background: radial-gradient(circle, rgba(0,0,0,0.035) 0%, rgba(0,0,0,0) 70%);
  }
  .card-back .emblem-area {
    left: 0; top: 30px; width: 370px; height: 370px;
    background: radial-gradient(circle, rgba(255,255,255,0.12) 0%, rgba(255,255,255,0) 70%);
  }

  .brand {
    position: absolute; right: 32px; text-align: right;
    font-weight: 300; color: var(--brand-red);
  }
  .brand-name {
    display: flex; align-items: center; justify-content: flex-end; gap: 14px;
    font-size: 46px; letter-spacing: 1px; line-height: 1;
    padding-bottom: 6px; border-bottom: 1px solid currentColor;
  }
  .brand-dot { width: 26px; height: 26px; border-radius: 50%; background: currentColor; }
  .brand-tagline { font-size: 17px; letter-spacing: 0.5px; margin-top: 6px; }
  .card-front .brand { top: 60px; }
  .card-back .brand { top: 275px; color: var(--ghost-white); }

  .person { position: absolute; left: 33px; top: 210px; }
  .person-name { font-weight: 700; font-size: 21px; color: var(--brand-red); letter-spacing: 0.3px; }
  .person-role { font-size: 15px; color: var(--text-dark); margin-top: 2px; }

  .divider {
    position: absolute; left: 33px; top: 278px; width: 452px; height: 1px;
    background: var(--rule-grey);
  }

  .address {
    position: absolute; left: 33px; top: 296px;
    font-size: 16px; line-height: 27px; color: var(--text-dark);
  }
  .contacts {
    position: absolute; right: 32px; top: 266px;
    list-style: none; text-align: right;
    font-size: 16px; line-height: 27px; color: var(--text-dark);
  }
  .contacts li { display: flex; justify-content: flex-end; align-items: center; gap: 6px; }
  .contacts svg { width: 15px; height: 15px; fill: var(--brand-red); }
</style>
</head>
<body>
<main class="canvas">

  <section class="card card-front">
    <div class="emblem-area" role="img" aria-label="Faint brand emblem watermark"></div>

    <div class="brand">
      <div class="brand-name"><span class="brand-dot"></span>VORNALY</div>
      <div class="brand-tagline">HEALTH CARE MARKETING</div>
    </div>

    <div class="person">
      <div class="person-name">MARNIE OKONSKI</div>
      <div class="person-role">CEO</div>
    </div>

    <div class="divider"></div>

    <address class="address" style="font-style:normal">
      Level 14, 8 Marlowe Tower<br>
      Sydney, 20, New South Wales
    </address>

    <ul class="contacts">
      <li>(502)638-2947
        <svg viewBox="0 0 16 16" aria-hidden="true"><path d="M2 5c0-2 2-3 6-3s6 1 6 3v1h-3V5H5v1H2z M4 7h8l2 6H2z"/></svg>
      </li>
      <li>marnie@vornaly.com
        <svg viewBox="0 0 16 16" aria-hidden="true"><path d="M1 3h14v10H1z M2 4l6 5 6-5" stroke="#fff" stroke-width="1.2"/></svg>
      </li>
      <li>www.vornaly.com
        <svg viewBox="0 0 16 16" aria-hidden="true"><circle cx="8" cy="8" r="7"/><path d="M1 8h14M8 1c3 3 3 11 0 14M8 1c-3 3-3 11 0 14" stroke="#fff" stroke-width="1" fill="none"/></svg>
      </li>
    </ul>
  </section>

  <section class="card card-back">
    <div class="emblem-area" role="img" aria-label="Large translucent brand emblem decoration"></div>
    <div class="brand">
      <div class="brand-name"><span class="brand-dot"></span>VORNALY</div>
      <div class="brand-tagline">HEALTH CARE MARKETING</div>
    </div>
  </section>

</main>
</body>
</html>
```